Banner Ad to promote Youth Cycling Camps

We need a 728 x 90 banner ad to promote some youth cycling camps. There are 2 different camps - a road camp where they learn to ride their bikes on the roads and a mountain bike camp. The camps teach bike handling skills and racing tactics.

Target Market(s)

Parents of youth ages 7-17

Industry/Entity Type

Non-Profit

Font styles to use
Sans Serif

Requirements
Must have
• Logo
• Dates - Road Camp May 5-7, 2017
• - Mountain Bike Camp July 14-16, 2017
• website - pedalwaycircuit.org
• be 728 x 90
Nice to have
• Animated - would like it to rotate with 3 slides - 1 a focus on both camps, 1 on road camp, 1 on mountain bike camp

```html
<!DOCTYPE html>
<html lang="en">
<head>
<meta charset="utf-8">
<title>Pedalway Circuit – Road Camp Banner</title>
<link rel="stylesheet" href="https://fonts.googleapis.com/css2?family=Montserrat:wght@400;600;700&display=swap">
<style>
  :root {
    --magenta: #e3197f;
    --magenta-deep: #c80f6c;
    --magenta-soft: #ee4d9c;
    --teal: #2fc4c6;
    --white: #ffffff;
    --photo-sky: #6c8fc4;
    --photo-green: #5d7a45;
    --photo-rider: #2e3f8a;
  }
  * { margin: 0; padding: 0; box-sizing: border-box; }
  html, body {
    width: 1200px;
    height: 148px;
    overflow: hidden;
    background: var(--white);
  }
  .banner {
    position: relative;
    width: 1200px;
    height: 148px;
    overflow: hidden;
    font-family: "Montserrat", Arial, sans-serif;
    color: var(--white);
    background:
      radial-gradient(ellipse 420px 120px at 640px 40px, rgba(255,255,255,0.10), transparent 70%),
      linear-gradient(100deg, var(--magenta-deep) 0%, var(--magenta) 45%, var(--magenta-soft) 75%, var(--magenta) 100%);
  }
  .rider-photo {
    position: absolute;
    inset: 0;
    width: 100%;
    height: 100%;
  }
  .camp-info {
    position: absolute;
    left: 490px;
    top: 14px;
  }
  .camp-dates {
    font-weight: 700;
    font-size: 60px;
    line-height: 72px;
    letter-spacing: 0.5px;
  }
  .camp-name {
    font-weight: 400;
    font-size: 43px;
    line-height: 52px;
    margin-top: 2px;
  }
  .brand {
    position: absolute;
    right: 18px;
    top: 14px;
    display: flex;
    align-items: center;
    gap: 8px;
  }
  .brand-dot {
    width: 22px;
    height: 22px;
    border-radius: 50%;
    background: var(--teal);
    flex: none;
  }
  .brand-name {
    font-weight: 600;
    font-size: 19px;
    line-height: 22px;
    color: var(--white);
  }
  .website {
    position: absolute;
    right: 18px;
    bottom: 10px;
    font-weight: 400;
    font-size: 21px;
    line-height: 24px;
  }
</style>
</head>
<body>
  <div class="banner">
    <svg class="rider-photo" viewBox="0 0 1200 148" aria-hidden="false">
      <defs>
        <linearGradient id="photoTone" x1="0" y1="0" x2="1" y2="1">
          <stop offset="0" stop-color="var(--photo-sky)"/>
          <stop offset="0.5" stop-color="var(--photo-rider)"/>
          <stop offset="1" stop-color="var(--photo-green)"/>
        </linearGradient>
      </defs>
      <polygon points="0,0 412,0 372,148 0,148" fill="url(#photoTone)"
               role="img" aria-label="Photo of a young racer in a helmet riding a bike"/>
      <polygon points="412,0 430,0 390,148 372,148" fill="var(--teal)"/>
    </svg>

    <div class="camp-info">
      <p class="camp-dates">May 5-7</p>
      <p class="camp-name">Road Camp</p>
    </div>

    <div class="brand">
      <span class="brand-dot"></span>
      <span class="brand-name">Pedalway<br>Circuit</span>
    </div>

    <p class="website">pedalwaycircuit.org</p>
  </div>
</body>
</html>
```